Preisliste für Kosmetikinstitut
Zielgruppe
Ich benötige für mein Kosmetikinstitut eine Preisliste für die moderne Frau, aber auch Männer. Das Design sollte mein Logo enthalten. Farben des Designkonzepts einbauen.
A4 quer zum Falten, wie ein Heft, 1. Seite Preisliste mit logo, im Innenteil dann Anwendungen
Aufgabenstellung
Minimalistisch, ästhetisch, modern, edel
Kontaktdaten auf der Rückseite
LT Hautatelier
Lena Tessmar
Lindenstieg 17
83671 Ostermoor
EMail: lena@lt-hautatelier.de
Whatsapp: 0176 284 9017

```html
<!DOCTYPE html>
<html lang="de">
<head>
<meta charset="utf-8">
<title>LT Hautatelier – Preisliste</title>
<link href="https://fonts.googleapis.com/css2?family=Poppins:wght@400;500;600;700&family=Allura&display=swap" rel="stylesheet">
<style>
:root{
  --bg:#a4a4a4;
  --cream:#fbfaee;
  --beige:#e8e5d5;
  --slate:#62716d;
  --slate-light:#8a9894;
  --mist:#e4e5df;
  --text:#3f4442;
  --row:#efede4;
}
*{box-sizing:border-box;margin:0;padding:0}
html,body{width:1091px;height:1200px;overflow:hidden}
body{background:var(--bg);font-family:"Poppins",sans-serif;color:var(--text);position:relative}
.page{position:absolute;width:379px;height:533px;background:var(--cream);overflow:hidden;box-shadow:0 3px 10px rgba(0,0,0,.3)}
.page--cover{left:150px;top:67px}
.page--inner{left:546px;top:67px}
.page--back{left:356px;top:618px}
.edge{position:absolute;top:0;bottom:0;width:14px;background:var(--beige)}
.edge--l{left:0}.edge--r{right:0}
.deco{position:absolute;left:0;width:379px}
.brand{position:absolute;text-align:center;font-weight:500;color:var(--slate);letter-spacing:.5px}
.brand__dot{display:inline-block;width:9px;height:9px;border-radius:50%;background:var(--slate);margin-right:6px;vertical-align:middle}
.contact{position:absolute;left:0;right:0;text-align:center;font-size:6.5px;line-height:9px;color:var(--text)}
.contact b{font-weight:600;color:var(--slate)}
.cover-title{position:absolute;left:0;right:0;top:100px;text-align:center;font-family:"Allura",cursive;font-size:60px;color:var(--slate);line-height:1}
.section{position:absolute;left:42px;width:296px;height:25px;border:2px solid var(--slate);border-radius:4px;background:var(--cream);text-align:center;font-weight:700;font-size:15px;line-height:21px;color:var(--slate)}
.item{position:absolute;left:42px}
.item__name{font-weight:700;font-size:8.5px;line-height:10px;color:var(--slate)}
.item__text{font-size:5.8px;line-height:7.6px;margin-top:3px;color:var(--text)}
.rule{position:absolute;width:1px;background:var(--slate)}
.tag{position:absolute;display:flex;height:13px;border:1px solid var(--slate);font-weight:700;font-size:8.5px;line-height:11px;white-space:nowrap}
.tag__label{background:var(--slate);color:#fff;padding:0 4px;text-align:center}
.tag__price{background:var(--cream);color:var(--slate);padding:0 4px;flex:1;text-align:center}
.steps{position:absolute;left:42px;width:296px;font-size:5.8px;line-height:7.6px;list-style:none}
.steps li{display:flex}
.steps b{width:9px;flex:none;color:var(--slate)}
.extras{position:absolute;left:42px;top:210px;width:296px;font-size:7.5px}
.extras div{display:flex;justify-content:space-between;padding:3px 8px;min-height:15px}
.extras div:nth-child(odd){background:var(--row)}
.extras span:last-child{font-weight:700;width:40px}
.photo{position:absolute;left:0;top:370px;width:379px;height:150px;background:linear-gradient(120deg,#c9b8a8 0%,#e8ddd4 35%,#f3efea 60%,#d6d2cc 100%)}
</style>
</head>
<body>

<section class="page page--cover">
  <div class="edge edge--l"></div><div class="edge edge--r"></div>
  <svg class="deco" style="top:0" height="200" viewBox="0 0 379 200">
    <defs><linearGradient id="mist1" x1="0" y1="0" x2="1" y2="1"><stop offset="0" stop-color="#dcdfd8"/><stop offset="1" stop-color="#eeefe8"/></linearGradient></defs>
    <path d="M0 0H379V55C300 92 210 92 140 80C80 70 35 85 0 112Z" fill="url(#mist1)"/>
    <path d="M0 112C35 85 80 70 140 80C210 92 300 92 379 55V57C300 98 210 98 140 88C80 80 35 95 0 118Z" fill="var(--beige)"/>
    <path d="M0 127C30 100 80 87 140 94C220 103 310 100 379 70V55C300 98 210 98 140 88C80 80 35 95 0 118Z" fill="var(--slate)"/>
  </svg>
  <div class="brand" style="left:0;right:0;top:34px;font-size:15px"><span class="brand__dot"></span>LT Hautatelier</div>
  <div class="cover-title">Preisliste</div>
  <div class="section" style="top:164px">Gesichtsbehandlungen</div>
  <div class="rule" style="left:230px;top:201px;height:301px"></div>

  <div class="item" style="top:208px;width:180px">
    <div class="item__name">Express Facial Treatment</div>
    <div class="item__text">Für alle, die wenig Zeit haben und trotzdem ihre Haut auffrischen und revitalisieren wollen.<br><br>Reinigung, Enzympeeling, Serum, Maske, Abschlusspflege</div>
  </div>
  <div class="tag" style="left:243px;top:202px;width:95px"><span class="tag__label">35-45 Min.</span><span class="tag__price">€ 59,00</span></div>

  <div class="item" style="top:266px;width:170px">
    <div class="item__name">Classic Facial Treatment –<br>Klassische Gesichtsbehandlung</div>
    <div class="item__text">Reinigung, Enzympeeling, Vapozon, Ausreinigung, Augenbrauenkorrektur, Ampulle, Maske, individuelle Abschlusspflege</div>
  </div>
  <div class="tag" style="left:243px;top:260px;width:95px"><span class="tag__label">45-60 Min.</span><span class="tag__price">€ 89,00</span></div>

  <div class="item" style="top:324px;width:170px">
    <div class="item__name">Clear Skin Treatment</div>
    <div class="item__text">Die Haut wirkt ausgeglichener, Unreinheiten wird vorgebeugt, der Teint erhält Balance und kann sich beruhigen.<br>Gleichzeitig wird die Haut durch die Hyaluronsäure vitalisiert und Falten und Fältchen kann entgegengewirkt werden.</div>
  </div>
  <div class="tag" style="left:243px;top:318px;width:95px"><span class="tag__label">50-60 Min.</span><span class="tag__price">€ 89,00</span></div>

  <div class="item" style="top:395px;width:175px">
    <div class="item__name">Rosaline Treatment</div>
    <div class="item__text">Hautrötungen und Couperose Erscheinungen werden gelindert, die Gefäßwände werden gestärkt und das Hautbild wirkt ausgeglichener, mögliche Irritationen gehen zurück. Gleichzeitig sorgt die hochkonzentrierte Hyaluronsäure für Frische, Vitalität und Glätte.</div>
  </div>
  <div class="tag" style="left:243px;top:389px;width:95px"><span class="tag__label">50-60 Min.</span><span class="tag__price">€ 89,00</span></div>

  <div class="item" style="top:457px;width:175px">
    <div class="item__name">Calmisan Soft Treatment<br>(für die empfindliche, gereizte Haut)</div>
    <div class="item__text">Entzündliche Prozesse können gemildert werden, gereizte Haut oder solche, die wenig verträgt, wird beruhigt. Irritationen können zurückgehen, die Haut erhält Balance.</div>
  </div>
  <div class="tag" style="left:241px;top:451px;width:97px"><span class="tag__label">ca. 50 Min.</span><span class="tag__price">€ 79,00</span></div>
</section>

<section class="page page--inner">
  <div class="edge edge--l"></div><div class="edge edge--r"></div>
  <svg class="deco" style="top:0" height="260" viewBox="0 0 379 260">
    <defs><linearGradient id="mist2" x1="0" y1="0" x2="1" y2="1"><stop offset="0" stop-color="#f1f1ea"/><stop offset="1" stop-color="#e3e5de"/></linearGradient></defs>
    <path d="M14 0H365V180C300 215 220 215 150 203C90 193 40 200 14 215Z" fill="url(#mist2)"/>
    <path d="M0 250C30 215 80 200 150 207C230 216 310 222 379 178V187C310 230 230 225 150 214C80 206 35 220 0 258Z" fill="var(--slate)"/>
    <path d="M0 240C30 208 80 195 150 201C230 210 310 214 379 172V178C310 220 230 216 150 207C80 200 30 215 0 250Z" fill="var(--beige)"/>
  </svg>
  <div class="rule" style="left:227px;top:29px;height:82px"></div>

  <div class="item" style="top:31px;width:175px">
    <div class="item__name">Vitamin Soft Boost</div>
    <div class="item__text">Vitamine sorgen für Power und Frische in und auf der Haut, die Widerstandskraft der Haut wird gestärkt. Die Faltentiefe kann gemildert werden.</div>
  </div>
  <div class="tag" style="left:240px;top:29px;width:97px"><span class="tag__label">ca. 50 Min.</span><span class="tag__price">€ 79,00</span></div>

  <div class="item" style="top:86px;width:180px">
    <div class="item__name">Anti-Age Advanced</div>
    <div class="item__text">Die Haut wirkt insgesamt erfrischt, vitalisiert und gestrafft. Feine Linien und Fältchen werden reduziert.</div>
  </div>
  <div class="tag" style="left:243px;top:84px;width:94px"><span class="tag__label">50-70 Min.</span><span class="tag__price">€ 99,00</span></div>
  <div style="position:absolute;left:247px;top:100px;font-size:4.5px">(je nach Peeling)</div>

  <div class="item" style="top:132px;width:296px">
    <div class="item__name">Chemisches Peeling (Oktober – April)</div>
    <div class="item__text">Professionelle Peelings können viele Problemstellungen lindern, verbessern oder gar beheben. Dazu gehören die Zellerneuerung, Glättung der Hauttextur, Reduzierung von Pigmentflecken, Verbesserung von Akne</div>
  </div>

  <div class="section" style="top:246px">Apparative Behandlungen</div>

  <div class="item" style="top:286px;width:190px">
    <div class="item__name">AQUAclear – „Glowing Skin“ Treatment</div>
    <div class="item__text">In 6 Schritten zu einer Haut mit einmaligem Glow- Effekt</div>
  </div>
  <div class="tag" style="left:235px;top:285px;width:102px"><span class="tag__label">60 Minuten</span><span class="tag__price">€ 140,00</span></div>

  <ol class="steps" style="top:315px">
    <li><b>1.</b>Behandlungsschritt: die Haut wird tiefengereinigt</li>
    <li><b>2.</b>Behandlungsschritt: die obersten Verhornungen und Schuppen werden sanft mit einem Peeling gelöst</li>
    <li><b>3.</b>Behandlungsschritt: die Haut wird in der Tiefe gereinigt und entschlackt</li>
    <li><b>4.</b>Behandlungsschritt: niedermolekulare Wirkstoffe werden aufgebracht, um die Haut zu erfrischen und den entsprechenden Glow zu geben</li>
    <li><b>5.</b>Ausgewählte und hochdosierte Wirkstoffessenzen werden auf die Haut gesprüht und durch die niedrige Molekularstruktur können diese tiefer in der Haut wirken</li>
    <li><b>6.</b>Zum Schluss werden die Essenzen durch eine Impulsgebende Druckluftmassage noch tiefer in die Haut gebracht</li>
  </ol>

  <div class="item" style="top:411px;width:296px">
    <div class="item__name">Mikrodermabrasion</div>
    <div class="item__text">Bei der Mikrodermabrasion handelt es sich um ein mechanisches Hautpeeling, dabei werden mittels feinster Kristalle die Hornzellen der obersten Hautschicht schonend abgetragen und dann mit Hilfe eines Unterdrucks behutsam abgesaugt. Der revitalisierende Prozess erhöht die Durchblutung, fördert die Zellerneuerung und verleiht ihrer Haut ein zartes frisches Gefühl. Die Haut gewinnt an Spannkraft, feine Fältchen werden gemildert und Poren sichtbar verkleinert. Außerdem hilft es bei oberflächlichen Akne Narben, Pigmentstörungen und Dehnungsstreifen. Wirkstoffe können nun wieder besser von der Haut aufgenommen werden.</div>
  </div>
  <div class="tag" style="left:42px;top:491px;width:107px"><span class="tag__label" style="flex:1">Gesicht</span><span class="tag__price" style="flex:none;width:45px">€ 89,00</span></div>
  <div class="tag" style="left:157px;top:491px;width:181px"><span class="tag__label" style="flex:1">Gesicht, Hals, Dekolleté</span><span class="tag__price" style="flex:none;width:45px">€ 110,00</span></div>
</section>

<section class="page page--back">
  <div class="edge edge--l"></div><div class="edge edge--r"></div>

  <div class="item" style="top:28px;width:290px">
    <div class="item__name">Microneedling</div>
    <div class="item__text">Die Behandlung eignet sich besonders für Menschen, die ihre Hautqualität verbessern und Falten, (Akne)Narben, Pigmentverschiebungen, große Poren und sogar Haarausfall behandeln wollen.<br><br>Mit Hilfe feinster Nadeln werden der Haut kontrolliert Mikroverletzungen zugeführt, dies regt die natürliche Wundheilung, sowie Kollagen- und Elastin Bildung an. Microneedling ist also eine natürliche Beauty-Behandlung, die körpereigene Reparaturmechanismen nutzt, um ein strafferes Hautbild zu erhalten. Bereits nach der ersten Behandlung sieht die Haut aufgepolstert, frisch und rosig aus. Kleine Linien und Fältchen werden tiefenbehandelt. Die Haut wirkt straffer und jugendlicher. Ein weiterer Vorteil, durch die Stichkanäle können Wirkstoffe besser von der Haut aufgenommen werden.</div>
  </div>
  <div class="tag" style="left:42px;top:138px;width:106px"><span class="tag__label" style="flex:1">Gesicht</span><span class="tag__price" style="flex:none;width:47px">€ 110,00</span></div>
  <div class="tag" style="left:157px;top:138px;width:181px"><span class="tag__label" style="flex:1">Gesicht, Hals, Dekolleté</span><span class="tag__price" style="flex:none;width:47px">€ 150,00</span></div>
  <div class="tag" style="left:42px;top:156px;width:141px"><span class="tag__label" style="flex:1">Gesicht, Hals</span><span class="tag__price" style="flex:none;width:50px">€ 130,00</span></div>

  <div class="item" style="top:197px"><div class="item__name">Zusatzleistungen</div></div>
  <div class="extras">
    <div><span>Augenbrauen zupfen</span><span>€ 8</span></div>
    <div><span>Augenbrauen färben</span><span>€ 12</span></div>
    <div><span>Wimpern färben</span><span>€ 15</span></div>
    <div><span>Enthaarung störender Gesichtsbehaarung<br>mittels Wax</span><span>€ 10-30</span></div>
  </div>

  <div class="brand" style="left:0;right:0;top:292px;font-size:15px"><span class="brand__dot"></span>LT Hautatelier</div>
  <address class="contact" style="top:313px;font-style:normal">
    <b>Lena Tessmar</b> · Lindenstieg 17 · 83671 Ostermoor<br>
    E-Mail: lena@lt-hautatelier.de · WhatsApp: 0176 284 9017
  </address>

  <div class="photo" role="img" aria-label="Foto: Kosmetikerin massiert das Gesicht einer entspannten Kundin auf der Behandlungsliege"></div>
  <svg class="deco" style="top:355px" height="178" viewBox="0 0 379 178">
    <path d="M0 0H379V25C300 12 220 15 150 25C90 33 40 40 0 80Z" fill="var(--cream)"/>
    <path d="M0 66C40 30 90 26 150 19C220 11 300 6 379 14V18C300 12 220 16 150 25C90 32 40 40 0 80Z" fill="var(--beige)"/>
    <path d="M0 75C40 40 90 32 150 25C220 17 300 12 379 17V27C300 20 220 24 150 33C90 40 40 50 0 88Z" fill="var(--slate)"/>
    <path d="M0 140C40 165 110 170 190 160C270 150 330 150 379 160V178H0Z" fill="var(--slate)"/>
    <path d="M0 135C40 160 110 165 190 155C270 145 330 145 379 155V160C330 150 270 150 190 160C110 170 40 165 0 140Z" fill="var(--cream)"/>
  </svg>
</section>

</body>
</html>
```